Business card for senior move management company
@ Project Holder : Could you extend this contest,please?
Is there latitude with the logo, can we remove the wavy lines if they interfere with the design?
All
there are some excellent design choices already, thank you!
General comments are:
1. The client has asked for her name to be in all capitals with the first letter of each word slightly larger than the rest.
2. The client for this company serves are tyically over 75 years old. The fonts need to be clearly legible, and as large as is practical. The phone number is especially important for size.
3. Vhange from the original spec: the website address should go with the text "Organizing, Downsizing and relocation management"
4. the text "Riverton, MA" should go with the phone number and email.
We are still interested in seeing additional creative ideas.
Thanks Again!
Gareth

```html
<!DOCTYPE html>
<html lang="en">
<head>
<meta charset="utf-8">
<title>Gentle Path Moves – Business Card</title>
<link rel="stylesheet" href="https://fonts.googleapis.com/css2?family=Source+Sans+3:wght@400;600&display=swap">
<style>
  :root {
    --page: #e9e6e1;
    --card-white: #ffffff;
    --navy: #15398a;
    --navy-deep: #0f2c74;
    --blue-mid: #1d4fa8;
    --blue-glow: #2f8ad8;
    --swoosh: #d9e3f2;
    --ink-blue: #1f4da0;
    --white: #ffffff;
  }
  * { margin: 0; padding: 0; box-sizing: border-box; }
  html, body { width: 1200px; height: 878px; overflow: hidden; }
  body {
    background: var(--page);
    font-family: "Source Sans 3", Arial, sans-serif;
    position: relative;
  }
  .card {
    position: absolute;
    width: 629px;
    height: 360px;
    overflow: hidden;
    box-shadow: 0 4px 14px rgba(0,0,0,0.18);
  }
  .card--front { left: 115px; top: 67px; background: var(--card-white); }
  .card--back {
    left: 439px; top: 456px;
    background: radial-gradient(circle at 73% 53%, var(--blue-glow) 0%, var(--blue-mid) 32%, var(--navy-deep) 78%);
  }
  .front-shape { position: absolute; inset: 0; }

  .brand {
    position: absolute;
    display: flex;
    align-items: center;
    gap: 12px;
  }
  .brand__dot { width: 16px; height: 16px; border-radius: 50%; flex: none; }
  .brand__name {
    font-weight: 600;
    text-transform: uppercase;
    letter-spacing: 1px;
    line-height: 1.1;
    font-size: 24px;
  }
  .brand--front { left: 30px; top: 62px; }
  .brand--front .brand__dot { background: var(--ink-blue); }
  .brand--front .brand__name { color: var(--ink-blue); }
  .brand--back { left: 370px; top: 150px; }
  .brand--back .brand__dot { background: var(--white); }
  .brand--back .brand__name { color: var(--white); }

  .services {
    position: absolute;
    left: 24px; top: 222px;
    color: var(--ink-blue);
  }
  .services__text { font-size: 21px; line-height: 1.2; }
  .services__web { font-size: 17px; margin-top: 8px; }

  .person {
    position: absolute;
    right: 20px; top: 14px;
    text-align: right;
    color: var(--white);
  }
  .person__name {
    font-size: 28px;
    font-variant: small-caps;
    letter-spacing: 0.5px;
    line-height: 1.1;
  }
  .person__title { font-size: 21px; }
  .contact {
    position: absolute;
    right: 26px; top: 204px;
    color: var(--white);
    line-height: 1.35;
  }
  .contact__phone { font-size: 30px; font-weight: 600; letter-spacing: 0.5px; }
  .contact__line { font-size: 17px; }
  .contact__city { font-size: 16px; text-align: right; }

  .tagline {
    position: absolute;
    left: 28px; top: 36px;
    color: var(--white);
    font-size: 24px;
  }
  .back-web {
    position: absolute;
    right: 22px; bottom: 18px;
    color: var(--white);
    font-size: 17px;
  }
</style>
</head>
<body>
  <section class="card card--front">
    <svg class="front-shape" viewBox="0 0 629 360" preserveAspectRatio="none" aria-hidden="true">
      <path d="M364 0 C404 170 364 280 248 360 L629 360 L629 0 Z" fill="var(--swoosh)"/>
      <path d="M380 0 C420 170 380 280 270 360 L629 360 L629 0 Z" fill="var(--navy)"/>
      <path d="M629 150 C540 200 460 280 410 360 L370 360 C440 260 540 180 629 122 Z" fill="var(--blue-mid)" opacity="0.6"/>
    </svg>

    <div class="brand brand--front">
      <span class="brand__dot"></span>
      <span class="brand__name">Gentle Path<br>Moves</span>
    </div>

    <div class="services">
      <p class="services__text">Organizing, Downsizing &amp;<br>Relocation Management</p>
      <p class="services__web">www.GPMtransitions.com</p>
    </div>

    <div class="person">
      <p class="person__name">Marla Quinn</p>
      <p class="person__title">President</p>
    </div>

    <div class="contact">
      <p class="contact__phone">555.318.2047</p>
      <p class="contact__line">marla@GPMtransitions.com</p>
      <p class="contact__city">Riverton, MA</p>
    </div>
  </section>

  <section class="card card--back">
    <p class="tagline">You and Your Belongings on a Gentle Path</p>
    <div class="brand brand--back">
      <span class="brand__dot"></span>
      <span class="brand__name">Gentle Path<br>Moves</span>
    </div>
    <p class="back-web">www.GPMtransitions.com</p>
  </section>
</body>
</html>
```